Interior Design & consultancy firm requires a new business card design that is a little bit funky bu

Kestrova Design Services is a leading strategic design practice specialising in the development and implementation of strategies and design solutions for commercial workplaces across a wide variety of industries.

The company has over twenty years experience in the strategic design, development and construction of innovative and efficient workplace environments for the commercial, corporate and industrial sectors.

We believe good design and efficient workspaces can transform companies, improve people’s lives and increase productivity.

Target Market(s)

My clients are mainly Government or corporate clients wanting to create a statement with their office fitout & new furniture that reflects their corporate identity

Industry/Entity Type

Construction

Font styles to use
Sans Serif

Colors
add136

Requirements
Must have
• The business card must be easy to read, simple & highlight my name & mobile phone number
Should not have
• I do not want the card to be fussy, feature too many colours or look to busy.

```html
<!DOCTYPE html>
<html lang="en">
<head>
<meta charset="utf-8">
<title>Nadia Pemberton — Kestrova Design Services</title>
<link rel="stylesheet" href="https://fonts.googleapis.com/css2?family=Orbitron:wght@600;700&family=Exo:wght@500&display=swap">
<style>
  :root {
    --lime: #a8ff00;
    --lime-line: #add136;
    --lime-edge: #8fcc00;
    --ink: #0d0d0d;
    --paper-light: #ffffff;
    --paper-edge: #dde2e2;
  }
  html, body {
    margin: 0;
    padding: 0;
    width: 1200px;
    height: 720px;
    overflow: hidden;
    background: var(--paper-edge);
  }
  .business-card {
    display: block;
    width: 1200px;
    height: 720px;
  }
  .name-title {
    font-family: "Orbitron", sans-serif;
    font-weight: 700;
    fill: var(--ink);
  }
  .mobile-number {
    font-family: "Orbitron", sans-serif;
    font-weight: 700;
    fill: var(--ink);
  }
  .side-label {
    font-family: "Exo", sans-serif;
    font-weight: 500;
    font-size: 23px;
    fill: var(--ink);
  }
  .role-line {
    font-family: "Exo", sans-serif;
    font-weight: 500;
    font-size: 22px;
    fill: var(--ink);
  }
  .tile { fill: var(--lime); }
  .tile-inset {
    fill: var(--lime);
    stroke: var(--lime-edge);
    stroke-width: 1.5;
  }
  .divider-rule {
    stroke: var(--lime-line);
    stroke-width: 1.6;
  }
</style>
</head>
<body>
<svg class="business-card" viewBox="0 0 1200 720" xmlns="http://www.w3.org/2000/svg">
  <defs>
    <radialGradient id="paper-glow" cx="0.58" cy="0.44" r="0.7">
      <stop offset="0" stop-color="var(--paper-light)"/>
      <stop offset="0.45" stop-color="#f4f5f5"/>
      <stop offset="1" stop-color="var(--paper-edge)"/>
    </radialGradient>
    <filter id="tile-shadow" x="-10%" y="-10%" width="120%" height="120%">
      <feDropShadow dx="1" dy="2" stdDeviation="1.2" flood-color="#000" flood-opacity="0.45"/>
    </filter>
    <filter id="inset-shadow" x="-10%" y="-10%" width="120%" height="120%">
      <feDropShadow dx="0" dy="1.5" stdDeviation="1.2" flood-color="#5c8a00" flood-opacity="0.55"/>
    </filter>
  </defs>

  <rect class="paper" width="1200" height="720" fill="url(#paper-glow)"/>

  <!-- brand tiles -->
  <g class="brand-tiles">
    <rect class="tile" x="50" y="69" width="272" height="217" rx="22" filter="url(#tile-shadow)"/>
    <rect class="tile-inset" x="150" y="126" width="152" height="121" rx="20" filter="url(#inset-shadow)"/>

    <rect class="tile" x="50" y="306" width="272" height="335" rx="22" filter="url(#tile-shadow)"/>
    <rect class="tile-inset" x="77" y="457" width="220" height="126" rx="20" filter="url(#inset-shadow)"/>
  </g>

  <!-- company name, set vertically -->
  <text class="side-label" transform="translate(44 256) rotate(-90)" textLength="100" lengthAdjust="spacingAndGlyphs">Services</text>
  <text class="side-label" transform="translate(44 617) rotate(-90)" textLength="185" lengthAdjust="spacingAndGlyphs">Kestrova  Design</text>

  <!-- name and mobile -->
  <text class="name-title" x="395" y="289" font-size="72" textLength="728" lengthAdjust="spacingAndGlyphs">NADIA PEMBERTON</text>
  <line class="divider-rule" x1="322" y1="296" x2="1190" y2="296"/>
  <text class="mobile-number" x="461" y="336" font-size="40" textLength="536" lengthAdjust="spacing" xml:space="preserve">0 4 9 1   5 7 0   1 5 6</text>

  <!-- role -->
  <g class="role" text-anchor="middle">
    <text class="role-line" x="755" y="589">director</text>
    <text class="role-line" x="755" y="614">&amp;</text>
    <text class="role-line" x="769" y="638" xml:space="preserve">senior  interior designer</text>
  </g>
</svg>
</body>
</html>
```